Business Card for Industrial Distributor

We need a business card design for an industrial distributor. We sell machine parts for the manufacturing and oil industry. We would like the cards to look clean and modern but with a touch of industry.

Our colors are blue/white.

Please feel free to visit our website www.krovelmint.com

Target Market(s)

mexican manufacturers in the automobile/aerospace industry

Industry/Entity Type

Industrial

Colors
ffffff
0555a3

```html
<!DOCTYPE html>
<html lang="en">
<head>
<meta charset="utf-8">
<title>Krovelmint Business Card</title>
<link rel="stylesheet" href="https://fonts.googleapis.com/css2?family=Roboto:wght@400;500;700&display=swap">
<style>
  :root {
    --stage: #2a2a2a;
    --white: #ffffff;
    --navy: #2b3990;
    --blue: #1a75bc;
    --ink: #222222;
  }
  * { box-sizing: border-box; margin: 0; padding: 0; }
  html, body { width: 1200px; height: 900px; overflow: hidden; }
  body {
    position: relative;
    background: var(--stage);
    font-family: "Roboto", Arial, sans-serif;
  }
  .card {
    position: absolute;
    left: 271px;
    width: 650px;
    height: 381px;
    border-radius: 18px;
    overflow: hidden;
    background: var(--white);
    box-shadow: 0 6px 14px rgba(0,0,0,0.45);
  }
  .card-front { top: 49px; }
  .card-back {
    top: 465px;
    background: radial-gradient(ellipse 60% 70% at 50% 35%, var(--blue) 0%, var(--navy) 100%);
  }

  /* front */
  .hero-circle {
    position: absolute;
    left: 374px;
    top: -9px;
    width: 330px;
    height: 330px;
    border-radius: 50%;
    background: radial-gradient(circle at 60% 30%, var(--blue) 0%, var(--navy) 85%);
  }
  .brand {
    position: absolute;
    display: flex;
    align-items: center;
    font-weight: 700;
    letter-spacing: -0.5px;
  }
  .brand-dot { border-radius: 50%; flex: none; }
  .card-front .brand { left: 34px; top: 54px; color: var(--navy); font-size: 48px; }
  .card-front .brand-dot {
    width: 56px; height: 56px; margin-right: 12px;
    background: radial-gradient(circle at 60% 35%, var(--blue), var(--navy));
  }
  .person { position: absolute; left: 40px; top: 167px; }
  .person-name { font-size: 19px; font-weight: 500; color: var(--ink); line-height: 24px; }
  .person-role { font-size: 14px; color: var(--navy); line-height: 18px; }
  .contacts { position: absolute; left: 41px; top: 228px; list-style: none; }
  .contacts li {
    display: flex; align-items: center;
    height: 22px; font-size: 16px; color: var(--ink);
  }
  .contacts svg { width: 15px; height: 15px; margin-right: 7px; flex: none; }
  .address-band {
    position: absolute; left: 0; top: 335px; width: 100%; height: 30px;
    background: linear-gradient(90deg, var(--navy) 0%, var(--navy) 50%, var(--blue) 80%, var(--navy) 100%);
    color: var(--white); font-size: 16px; line-height: 30px; padding-left: 40px;
  }

  /* back */
  .card-back .brand {
    left: 0; width: 100%; top: 140px; justify-content: center;
    color: var(--white); font-size: 50px;
  }
  .card-back .brand-dot { width: 64px; height: 64px; margin-right: 12px; background: var(--white); }
  .web-band {
    position: absolute; left: 0; top: 313px; width: 100%; height: 28px;
    background: var(--white); color: var(--navy);
    text-align: center; font-size: 17px; line-height: 28px;
  }
  .base-strip { position: absolute; left: 0; top: 341px; width: 100%; height: 22px; background: var(--navy); }
  .base-edge { position: absolute; left: 0; top: 363px; width: 100%; height: 18px; background: var(--white); }
</style>
</head>
<body>
  <section class="card card-front">
    <div class="hero-circle"></div>
    <div class="brand"><span class="brand-dot"></span>Krovelmint</div>
    <div class="person">
      <p class="person-name">Daniel Reyes</p>
      <p class="person-role">Managing director</p>
    </div>
    <ul class="contacts">
      <li><svg viewBox="0 0 15 15"><rect width="15" height="15" rx="3" fill="#2b3990"/><path d="M4 3.5l2 0 .8 2-1.2 1a5 5 0 0 0 2.9 2.9l1-1.2 2 .8v2a1 1 0 0 1-1 1A7.5 7.5 0 0 1 3 4.5a1 1 0 0 1 1-1z" fill="#fff"/></svg>(555) 214-7730</li>
      <li><svg viewBox="0 0 15 15"><rect width="15" height="15" rx="3" fill="#2b3990"/><rect x="5" y="3" width="5" height="3" fill="#fff"/><rect x="3" y="6" width="9" height="4" rx="1" fill="#fff"/><rect x="5" y="9" width="5" height="3" fill="#fff" stroke="#2b3990" stroke-width=".6"/></svg>(555) 214-7731</li>
      <li><svg viewBox="0 0 15 15"><rect width="15" height="15" rx="3" fill="#2b3990"/><rect x="3" y="4.5" width="9" height="6" fill="#fff"/><path d="M3 4.5l4.5 3.5 4.5-3.5" fill="none" stroke="#2b3990" stroke-width=".9"/></svg>sales@krovelmint.co</li>
      <li><svg viewBox="0 0 15 15"><rect width="15" height="15" rx="3" fill="#2b3990"/><rect x="3" y="3.5" width="9" height="6" fill="#fff"/><rect x="5.5" y="10.5" width="4" height="1.2" fill="#fff"/></svg>www.krovelmint.com</li>
    </ul>
    <div class="address-band">4120 Corvane Mill Rd, Eastbrook, TX 78590</div>
  </section>

  <section class="card card-back">
    <div class="brand"><span class="brand-dot"></span>Krovelmint</div>
    <div class="web-band">www.krovelmint.com</div>
    <div class="base-strip"></div>
    <div class="base-edge"></div>
  </section>
</body>
</html>
```